Business Card Design

WE are looking for a premium quality Business Cards for a Law Firm . Copies of our current business card is attached.

Contact Information for Business Card

xyz

```html
<!DOCTYPE html>
<html lang="en">
<head>
<meta charset="utf-8">
<title>Ashcombe Lawyers – Business Cards</title>
<link rel="stylesheet" href="https://fonts.googleapis.com/css2?family=Montserrat:wght@400;500;600;700&display=swap">
<style>
  :root {
    --bg: #3a3a3a;
    --green: #0f2a1d;
    --green-deep: #08231a;
    --gold: #c49a4c;
    --white: #ffffff;
    --paper: #f7f7f5;
  }
  * { box-sizing: border-box; margin: 0; padding: 0; }
  html, body {
    width: 1200px; height: 1200px; overflow: hidden;
    background: var(--bg);
    font-family: "Montserrat", sans-serif;
  }
  .sheet {
    position: relative; width: 1200px; height: 1200px;
  }
  .card {
    position: absolute; left: 120px;
    width: 960px; height: 548px;
    border-radius: 40px; overflow: hidden;
    box-shadow: 0 18px 40px rgba(0,0,0,.45);
  }
  .card-front { top: 32px; background: var(--paper); }
  .card-back {
    top: 620px;
    background: linear-gradient(120deg, var(--green-deep) 0%, #11352a 55%, var(--green-deep) 100%);
  }
  .front-bands { position: absolute; inset: 0; }

  /* brand */
  .brand {
    position: absolute; display: flex; flex-direction: column; align-items: center;
  }
  .brand-circle {
    border: 6px solid var(--gold); border-radius: 50%;
  }
  .brand-name {
    font-weight: 600; letter-spacing: .08em; text-transform: uppercase;
    white-space: nowrap; line-height: 1;
  }
  .card-front .brand { left: 280px; top: 44px; width: 440px; }
  .card-front .brand-circle { width: 100px; height: 100px; margin-bottom: 18px; }
  .card-front .brand-name { color: var(--green); font-size: 34px; }

  .card-back .brand { left: 230px; top: 56px; width: 500px; }
  .card-back .brand-circle { width: 150px; height: 150px; margin-bottom: 28px; }
  .card-back .brand-name { color: var(--white); font-size: 44px; }

  /* front: person */
  .person {
    position: absolute; left: 58px; top: 382px; color: var(--white);
  }
  .person-name {
    color: var(--gold); font-weight: 700; font-size: 40px; letter-spacing: .02em; line-height: 1;
  }
  .person-role {
    margin-top: 8px; font-size: 14px; font-weight: 500; line-height: 1.25; letter-spacing: .02em;
  }
  .person-address {
    margin-top: 20px; font-size: 20px; line-height: 1.3;
  }

  /* front: contacts */
  .contacts {
    position: absolute; left: 570px; top: 300px; list-style: none; color: var(--white);
  }
  .contacts li {
    display: flex; align-items: center; gap: 12px;
    font-size: 18px; height: 40px;
  }
  .contact-icon {
    width: 30px; height: 30px; border-radius: 50%; background: var(--gold);
    display: flex; align-items: center; justify-content: center; flex: none;
  }
  .contact-icon svg { width: 17px; height: 17px; }

  /* back: offices */
  .offices {
    position: absolute; left: 70px; right: 60px; bottom: 46px;
    display: flex; justify-content: space-between; align-items: flex-end;
  }
  .office { color: var(--white); width: 380px; }
  .office-title {
    color: var(--gold); font-weight: 600; font-size: 17px; letter-spacing: .02em; margin-bottom: 6px;
  }
  .office-line {
    display: flex; align-items: flex-start; gap: 10px; font-size: 16px; line-height: 1.3; margin-top: 4px;
  }
  .office-line svg { width: 18px; height: 18px; flex: none; margin-top: 2px; }
  .office-divider {
    width: 1px; height: 110px; background: var(--gold); opacity: .7; align-self: center;
  }
</style>
</head>
<body>
<main class="sheet">

  <section class="card card-front">
    <svg class="front-bands" viewBox="0 0 960 548" preserveAspectRatio="none" aria-hidden="true">
      <polygon points="0,332 960,252 960,548 0,548" fill="#0f2a1d"/>
      <line x1="0" y1="318" x2="960" y2="238" stroke="#c49a4c" stroke-width="5"/>
    </svg>

    <div class="brand">
      <div class="brand-circle"></div>
      <div class="brand-name">Ashcombe Lawyers</div>
    </div>

    <div class="person">
      <div class="person-name">DANIEL MARSH</div>
      <div class="person-role">DIRECTOR &amp; PRINCIPAL SOLICITOR<br>MBA, JURIS DOCTOR</div>
      <div class="person-address">Level 3, Ashcombe House,<br>120 Ridge Terrace, Spring Hill, QLD 4000</div>
    </div>

    <ul class="contacts">
      <li>
        <span class="contact-icon"><svg viewBox="0 0 24 24"><path fill="#0f2a1d" d="M6.6 10.8a15 15 0 0 0 6.6 6.6l2.2-2.2a1 1 0 0 1 1-.25 11.4 11.4 0 0 0 3.6.6 1 1 0 0 1 1 1V20a1 1 0 0 1-1 1A17 17 0 0 1 3 4a1 1 0 0 1 1-1h3.5a1 1 0 0 1 1 1c0 1.25.2 2.45.6 3.6a1 1 0 0 1-.25 1z"/></svg></span>
        +61 7 3000 4812
      </li>
      <li>
        <span class="contact-icon"><svg viewBox="0 0 24 24"><rect x="7" y="2" width="10" height="20" rx="2" fill="none" stroke="#0f2a1d" stroke-width="2"/><circle cx="12" cy="18" r="1.2" fill="#0f2a1d"/></svg></span>
        +61 0400 112 347
      </li>
      <li>
        <span class="contact-icon"><svg viewBox="0 0 24 24"><rect x="3" y="5" width="18" height="14" rx="1.5" fill="none" stroke="#0f2a1d" stroke-width="2"/><path d="M3 6l9 7 9-7" fill="none" stroke="#0f2a1d" stroke-width="2"/></svg></span>
        daniel@ashcombelawyers.com.au
      </li>
      <li>
        <span class="contact-icon"><svg viewBox="0 0 24 24"><circle cx="12" cy="12" r="9" fill="none" stroke="#0f2a1d" stroke-width="2"/><ellipse cx="12" cy="12" rx="4" ry="9" fill="none" stroke="#0f2a1d" stroke-width="1.6"/><path d="M3 12h18M5 7.5h14M5 16.5h14" stroke="#0f2a1d" stroke-width="1.4"/></svg></span>
        www.ashcombelawyers.com.au
      </li>
    </ul>
  </section>

  <section class="card card-back">
    <div class="brand">
      <div class="brand-circle"></div>
      <div class="brand-name">Ashcombe Lawyers</div>
    </div>

    <div class="offices">
      <div class="office">
        <div class="office-title">BRISBANE OFFICE</div>
        <div class="office-line">
          <svg viewBox="0 0 24 24"><path d="M12 2a7 7 0 0 0-7 7c0 5 7 13 7 13s7-8 7-13a7 7 0 0 0-7-7z" fill="none" stroke="#c49a4c" stroke-width="2.4"/><circle cx="12" cy="9" r="2.5" fill="#c49a4c"/></svg>
          <span>Level 3, Ashcombe House, 120<br>Ridge Terrace Spring Hill QLD 4000</span>
        </div>
        <div class="office-line">
          <svg viewBox="0 0 24 24"><path fill="#c49a4c" d="M6.6 10.8a15 15 0 0 0 6.6 6.6l2.2-2.2a1 1 0 0 1 1-.25 11.4 11.4 0 0 0 3.6.6 1 1 0 0 1 1 1V20a1 1 0 0 1-1 1A17 17 0 0 1 3 4a1 1 0 0 1 1-1h3.5a1 1 0 0 1 1 1c0 1.25.2 2.45.6 3.6a1 1 0 0 1-.25 1z"/></svg>
          <span>(07) 3000 4812</span>
        </div>
      </div>

      <div class="office-divider"></div>

      <div class="office">
        <div class="office-title">MELBOURNE OFFICE</div>
        <div class="office-line">
          <svg viewBox="0 0 24 24"><path d="M12 2a7 7 0 0 0-7 7c0 5 7 13 7 13s7-8 7-13a7 7 0 0 0-7-7z" fill="none" stroke="#c49a4c" stroke-width="2.4"/><circle cx="12" cy="9" r="2.5" fill="#c49a4c"/></svg>
          <span>Suite 210, Bramley Chambers, 318<br>Larch Street, Melbourne, VIC, 3000</span>
        </div>
        <div class="office-line">
          <svg viewBox="0 0 24 24"><path fill="#c49a4c" d="M6.6 10.8a15 15 0 0 0 6.6 6.6l2.2-2.2a1 1 0 0 1 1-.25 11.4 11.4 0 0 0 3.6.6 1 1 0 0 1 1 1V20a1 1 0 0 1-1 1A17 17 0 0 1 3 4a1 1 0 0 1 1-1h3.5a1 1 0 0 1 1 1c0 1.25.2 2.45.6 3.6a1 1 0 0 1-.25 1z"/></svg>
          <span>(07) 3000 4812</span>
        </div>
      </div>
    </div>
  </section>

</main>
</body>
</html>
```